Eyecatching website design for commercial lighting business

This contest is all about the graphic design aspect. We need a striking website design for a commercial lighting company. We want something really eye catching to introduce people to our range of induction and LED lights which save businesses money on maintenance and electricity costs.

To be successful in this contest you will need to provide a design and pictures for the pages listed below.

We are using the platform talvo.com.au and you can see the attached template which everything will be loaded into so we just need HTML files which we can upload and we can do everything else from Talvo.

The final design should be strong and clean and use the colours and textures in the attached business card file.

Detailed requirements:

Please see attached screenshot of the website template, all we need is a fantastic graphic design and improvement/ incorporation of our logo for the following pages
Page Headings:
1. Home
About Us, Contact Us, snapshot of and link to Blog

Each of the below pages will have several paragraphs of text followed by a list of suitable products which is generated from our product catalogue.

2. Car Park Lighting
3. Educational Lighting
4. Hospitality Lighting
5. Office & Shop Lighting
6. Warehouse Lighting

Some of the website we have seen which are similar in nature are:
http://www.quorbenlamps.com.au/
http://www.yimra.com/
http://www.brightvane.net/commercial-led
but we really want a modern, eye catching and memorable design

Some of the designs built on Talvo that we like are:

http://www.harbourmarket.com.au/
http://www.tacklebay.com.au/
http://www.wenbrook.com.au/

I've also uploaded a couple of photos that we love. We'd like something similar for each industry.

Target Market(s)

Company Owners, Maintenance & Facilities Managers, Electrical Contractors

Industry/Entity Type

Electrical

Coding

Coded - Design and coding required

Number of Pages Required

5+ page

Font styles to use
Sans Serif

Colors
33a6d7
ec1f27

Requirements
Must have
• -Must scale to mobile
• -HTML coded files need to be provided (HTML Bootstrap)
Nice to have
• -Prefer incorporation of our logo into header bar
• -Design of 2-3 advertising banners which can be displayed on the home page
• -Prominent call to action button towards top of page 'Get a quote' or similar
• -Grid based design HTML Bootstrap

```html
<!DOCTYPE html>
<html lang="en">
<head>
<meta charset="utf-8">
<title>K&amp;R Trade Solutions – Commercial Lighting</title>
<link href="https://fonts.googleapis.com/css2?family=Open+Sans:wght@400;600;700&family=Oswald:wght@500;600&display=swap" rel="stylesheet">
<style>
:root{
  --red:#c8161e;
  --red-dark:#7d0c10;
  --blue:#2f97cc;
  --blue-light:#33a6d7;
  --ink:#444;
  --muted:#777;
  --page:#eef0f1;
  --footer:#2b2b2b;
  --footer-dark:#1c1c1c;
}
*{box-sizing:border-box;margin:0;padding:0}
html,body{width:900px;height:1200px;overflow:hidden}
body{font-family:"Open Sans",Arial,sans-serif;color:var(--ink);background:var(--page);font-size:11px;line-height:1.5}
.header{height:88px;background:linear-gradient(180deg,#a30f16,var(--red-dark));position:relative;padding:0 60px}
.brand{position:absolute;left:60px;top:18px;display:flex;align-items:center;gap:10px}
.brand-mark{width:46px;height:46px;border-radius:50%;background:#fff}
.brand-name{font-family:"Oswald",sans-serif;font-weight:500;color:#fff;font-size:20px;line-height:1.05;letter-spacing:.5px}
.header-tools{position:absolute;right:60px;top:34px;display:flex;gap:10px;align-items:center}
.search{width:130px;height:22px;background:#fff;border-radius:2px;font-size:10px;color:#999;padding:3px 6px;display:flex;justify-content:space-between}
.cart{height:22px;background:#fff;border-radius:2px;font-size:10px;color:#555;padding:3px 8px}
.account{color:#fff;font-size:10px}
.nav{height:26px;background:var(--blue);padding:0 60px;display:flex}
.nav a{color:#fff;text-decoration:none;font-size:11px;padding:0 14px;line-height:26px}
.nav a.active{background:#fff;color:var(--blue);font-weight:600}
.content{display:flex;gap:22px;padding:22px 60px 0}
.sidebar{width:236px}
.box{background:#fff;margin-bottom:18px;border:1px solid #ddd}
.box h3{font-weight:400;font-size:15px;color:#fff;padding:5px 10px;background:var(--red)}
.box h3.blue{background:var(--blue)}
.box ul{list-style:none;padding:6px 10px}
.box li{color:var(--muted);font-size:12px;padding:6px 0;border-bottom:1px solid #eee}
.box li:last-child{border:none}
.box li::before{content:"›  ";color:var(--red)}
.history{display:flex;gap:10px;padding:12px 10px}
.history .thumb{width:60px;height:70px;background:linear-gradient(#555,#222)}
.history .name{color:var(--red);font-weight:600;font-size:11px;line-height:1.3}
.history .old{color:#999;text-decoration:line-through}
.history .now{color:var(--red);font-weight:700}
.ad{height:210px;background:linear-gradient(160deg,#9fd3ec,#e8f4fb 55%,#ffffff);position:relative;padding:12px;text-align:center}
.ad-title{font-family:"Oswald",sans-serif;font-size:19px;color:var(--red);line-height:1.1}
.ad-sub{font-size:12px;color:#123c6a;font-weight:700;line-height:1.2;margin-top:4px}
.ad-price{position:absolute;left:20px;top:100px;width:62px;height:62px;border-radius:50%;background:var(--red);color:#fff;font-weight:700;font-size:13px;line-height:1.1;padding-top:15px}
.ad-link{position:absolute;left:10px;bottom:10px;font-size:12px;font-weight:700;color:#123c6a}
.main{flex:1;background:#fff;padding:0 0 18px;border:1px solid #ddd}
.hero{height:245px;background:linear-gradient(180deg,#0d1830,#2a3c5e 55%,#4b7a64)}
.intro{padding:14px 18px 0}
.welcome{font-family:"Oswald",sans-serif;font-weight:600;font-size:34px;color:var(--red);line-height:1}
.subtitle{color:var(--blue);font-size:14px;margin:2px 0 10px}
.intro p{font-size:10.5px;color:var(--muted);margin-bottom:10px}
.lead{color:var(--red);font-size:15px;margin:6px 0 8px}
.ticks{list-style:none;margin-bottom:12px}
.ticks li{display:flex;gap:8px;align-items:flex-start;color:var(--blue);font-size:13px;margin-bottom:6px}
.ticks svg{flex:none;margin-top:2px}
.call{color:var(--red);font-size:15px;font-weight:600}
.footer{margin-top:22px;background:var(--footer);height:296px;padding:26px 60px 0;display:flex;gap:24px;position:relative}
.col{flex:1;color:#bbb;font-size:10px}
.col h4{font-weight:400;color:#fff;font-size:17px;margin-bottom:10px}
.col ul{list-style:none}
.col li{margin-bottom:4px}
.col li::before{content:"› ";color:var(--red)}
.contact div{display:flex;gap:6px;margin-bottom:6px}
.dot{width:9px;height:9px;border-radius:50%;background:var(--red);flex:none;margin-top:3px}
.legal{position:absolute;left:0;right:0;bottom:0;height:30px;background:var(--footer-dark);color:var(--red);font-size:9px;text-align:center;line-height:30px}
</style>
</head>
<body>
<header class="header">
  <div class="brand"><span class="brand-mark"></span><span class="brand-name">K&amp;R<br>TRADE SOLUTIONS</span></div>
  <div class="header-tools">
    <div class="search"><span>Search here...</span><span>⌕</span></div>
    <div class="cart">Empty Cart ▾</div>
    <div class="account">My Account ▾</div>
  </div>
</header>
<nav class="nav">
  <a class="active">Home</a><a>Car parking</a><a>Educational lighting</a><a>Office &amp; Shop lighting</a><a>Warehouse lighting</a><a>All products</a><a>Blog</a>
</nav>
<div class="content">
  <aside class="sidebar">
    <div class="box"><h3>Categories</h3><ul><li>Induction Lighting</li></ul></div>
    <div class="box"><h3 class="blue">Browse History</h3>
      <div class="history"><div class="thumb" role="img" aria-label="High bay light fitting"></div>
        <div><div class="name">150w Weatherproof High Bay - Natural Light</div><div class="old">$455.44</div><div class="now">$340.00</div><div style="color:#999;font-size:9px">RRP $556.60</div></div></div>
    </div>
    <div class="box"><h3>Information</h3><ul><li>About us</li><li>Return policy</li><li>Contact us</li></ul></div>
    <div class="ad" role="img" aria-label="Travel advertisement with snowy chalet scene">
      <div class="ad-title">Luxury Chalet Savings</div>
      <div class="ad-sub">Save up to $1200<br>on flights &amp; chalets</div>
      <div class="ad-price">7 Nts fr<br>$499pp</div>
      <div class="ad-link">Snowpeak Travel</div>
    </div>
  </aside>
  <main class="main">
    <div class="hero" role="img" aria-label="Floodlit outdoor sports courts at dusk"></div>
    <div class="intro">
      <div class="welcome">WELCOME TO</div>
      <div class="subtitle">the Commercial Lighting Division of K&amp;R Morton Trade Solutions</div>
      <p>Retrofitting the lighting in a commercial or industrial premises is a great way to save money on energy costs and maintenance, create a safer work environment and reduce the load on the wiring in the premises.</p>
      <p>When you are considering a retrofit of a commercial building there are a number of technologies on the market and a lot to consider.</p>
      <div class="lead">We make it an easy process by providing you with:</div>
      <ul class="ticks">
        <li><svg width="14" height="14" viewBox="0 0 14 14"><circle cx="7" cy="7" r="7" fill="#33a6d7"/><path d="M3.5 7.2l2.3 2.3 4.7-4.8" stroke="#fff" stroke-width="1.8" fill="none"/></svg>The best range of energy saving commercial &amp; industrial lighting</li>
        <li><svg width="14" height="14" viewBox="0 0 14 14"><circle cx="7" cy="7" r="7" fill="#33a6d7"/><path d="M3.5 7.2l2.3 2.3 4.7-4.8" stroke="#fff" stroke-width="1.8" fill="none"/></svg>High quality products from reputable manufacturers which meet Australian Standards</li>
        <li><svg width="14" height="14" viewBox="0 0 14 14"><circle cx="7" cy="7" r="7" fill="#33a6d7"/><path d="M3.5 7.2l2.3 2.3 4.7-4.8" stroke="#fff" stroke-width="1.8" fill="none"/></svg>Assistance to ensure you choose the right product for the right application</li>
      </ul>
      <p>Situated in Glen Harrow the Commercial Lighting Division of K&amp;R Morton Trade Solutions offers easy solutions for commercial retrofit of lighting throughout Victoria and we can also ship Australia wide.</p>
      <p>With a highly experienced team and a strong range of quality products our staff are available Monday to Friday 9am-5pm AEST to take <span class="call">Calls on (03) 9400 1188.</span></p>
    </div>
  </main>
</div>
<footer class="footer">
  <div class="col"><h4>Services</h4><ul><li>Car Park Lighting</li><li>Educational Lighting</li><li>Hospitality Lighting</li><li>Office &amp; Shop Lighting</li><li>Warehouse Lighting</li></ul></div>
  <div class="col"><h4>About Us</h4><p>Retrofitting the lighting in a commercial or industrial premises is a great way to save money on energy costs and maintenance, create a safer work environment and reduce the load on the wiring in the premises.</p></div>
  <div class="col"><h4>Information</h4><ul><li>About us</li><li>Return policy</li><li>Contact us</li></ul></div>
  <div class="col contact"><h4>Stay In Touch</h4>
    <div><span class="dot"></span>Glen Harrow, Victoria, Australia</div>
    <div><span class="dot"></span>(03) 9400 1188</div>
    <div><span class="dot"></span>info@krmortontrade.com.au</div>
  </div>
  <div class="legal">© K&amp;R Trade Solutions 2015. All Rights Reserved.</div>
</footer>
</body>
</html>
```